Corvid Lens Studio Business Card Design

I need a business card designed for a photography business based in Perth, Western Australia called Corvid Lens Studio.

We specialise in wedding, event photography and portrait photography.

The business card must borrow the style of the attached logo.

The hex codes for the colours in the logo are:
#ED1D85 - Pink
#89C23E - Green
#37282F - Black

The name on the card will be:
Name: Tobiah
Phone: 0417395268
Website: www.corvidlensstudio.com.au
friendsheet: corvidlensstudio

I am open and happy to accept creative concepts.

Industry/Entity Type

Business

```html
<!DOCTYPE html>
<html lang="en">
<head>
<meta charset="utf-8">
<title>Corvid Lens Studio – Business Card</title>
<link href="https://fonts.googleapis.com/css2?family=Questrial&display=swap" rel="stylesheet">
<style>
  :root {
    --backdrop: #e9e6e2;
    --card: #ffffff;
    --ink: #37282f;
    --ink-soft: #6d6468;
    --pink: #ed1d85;
    --green: #89c23e;
    --smoke-pink: rgba(214, 120, 150, 0.22);
    --smoke-grey: rgba(150, 140, 145, 0.16);
  }
  * { box-sizing: border-box; margin: 0; padding: 0; }
  html, body {
    width: 1200px; height: 1023px; overflow: hidden;
    background: var(--backdrop);
    font-family: "Questrial", "Century Gothic", sans-serif;
    color: var(--ink);
  }
  .card {
    position: absolute; left: 140px; top: 231px;
    width: 920px; height: 560px;
    background: linear-gradient(160deg, #ffffff 0%, #f6f5f5 100%);
    box-shadow: 0 14px 36px rgba(60, 40, 30, 0.22);
    overflow: hidden;
  }
  .smoke {
    position: absolute; inset: 0;
    background:
      radial-gradient(ellipse 380px 200px at 560px 120px, var(--smoke-pink), transparent 70%),
      radial-gradient(ellipse 300px 260px at 720px 400px, var(--smoke-pink), transparent 70%),
      radial-gradient(ellipse 420px 160px at 300px 450px, var(--smoke-grey), transparent 70%);
  }
  .identity {
    position: absolute; left: 60px; top: 56px;
    display: flex; align-items: center; gap: 24px;
  }
  .brand-mark {
    width: 96px; height: 96px; border-radius: 50%;
    background: var(--pink);
    flex: none;
  }
  .identity-text { display: flex; flex-direction: column; gap: 8px; }
  .brand-name {
    font-size: 22px; letter-spacing: 3px; text-transform: uppercase; color: var(--pink);
  }
  .name {
    font-size: 46px; letter-spacing: 6px; text-transform: uppercase; line-height: 1;
  }
  .website {
    position: absolute; left: 60px; top: 205px;
    font-size: 34px; letter-spacing: 7px; text-transform: uppercase; color: var(--ink-soft);
  }
  .swoosh { position: absolute; left: 0; top: 0; }
  .contact {
    position: absolute; left: 60px; display: flex; align-items: center; gap: 22px;
  }
  .contact-phone { top: 350px; font-size: 36px; letter-spacing: 5px; }
  .contact-social { top: 445px; font-size: 27px; letter-spacing: 1px; }
  .icon-social { width: 38px; height: 38px; border-radius: 50%; background: var(--pink); flex: none; }
</style>
</head>
<body>
  <main class="card">
    <div class="smoke" role="img" aria-label="Soft pink and grey flowing smoke background"></div>

    <div class="identity">
      <span class="brand-mark"></span>
      <div class="identity-text">
        <span class="brand-name">Corvid Lens Studio</span>
        <span class="name">Tobiah</span>
      </div>
    </div>

    <div class="website">www.corvidlensstudio.com.au</div>

    <svg class="swoosh" width="920" height="560" viewBox="0 0 920 560" aria-hidden="true">
      <path d="M60,330 C300,276 600,246 860,240 C600,258 320,294 60,330 Z" fill="#1a1416"/>
    </svg>

    <div class="contact contact-phone">
      <svg width="38" height="38" viewBox="0 0 24 24" aria-hidden="true">
        <path fill="var(--green)" d="M6.6 10.8a15.1 15.1 0 0 0 6.6 6.6l2.2-2.2c.3-.3.7-.4 1-.2 1.1.4 2.3.6 3.6.6.6 0 1 .4 1 1V20c0 .6-.4 1-1 1A17 17 0 0 1 3 4c0-.6.4-1 1-1h3.5c.6 0 1 .4 1 1 0 1.3.2 2.5.6 3.6.1.3 0 .7-.2 1l-2.3 2.2z"/>
      </svg>
      <span>0417 395 268</span>
    </div>

    <div class="contact contact-social">
      <span class="icon-social"></span>
      <span>www.friendsheet.com/corvidlensstudio</span>
    </div>
  </main>
</body>
</html>
```